Brindle Works - Fast, Efficient and Gas Mainteance for Domestic, Commercial and Industrial clients

We are in the process of purchasing a new business and would like to get a new logo and business card.
Business is a gas maintenance business that also does new gas installations.
Has been established since 1988.
Services include:
Install all types of gas appliances & equipment inc. hot water units
Maintain / repair / replace all types of gas appliances & equipment

Target Market(s)

Domestic, Commercial and Industrial clients

Industry/Entity Type

Business

Contact Information for Business Card

admin@brindleworks-example.com.au
07 5981 4726
Brindle Works PTY LTD

Logo Text

Gas Fitting & Plumbing Maintenance Specialists

Font styles to use
Sans Serif

Requirements
Must have
• Logo
• Business name, contact number, email address, web address
• Domestic | Commercial | Industrial Est Since 1988
Nice to have
• Possibly a black card with a flame logo to one side
Should not have
• Spelling errors

```html
<!DOCTYPE html>
<html lang="en">
<head>
<meta charset="UTF-8">
<title>Brindle Works – Business Cards</title>
<link rel="stylesheet" href="https://fonts.googleapis.com/css2?family=Figtree:wght@400;500;800&display=swap">
<style>
  :root {
    --page-bg: #ece9e5;
    --card-bg: #ffffff;
    --ink: #111111;
    --accent: #ee6a1c;
    --flame-red: #e8301f;
    --flame-orange: #f26a21;
    --flame-yellow: #f7a21b;
    --card-shadow: rgba(0, 0, 0, 0.18);
  }
  * { margin: 0; padding: 0; box-sizing: border-box; }
  html, body {
    width: 1200px;
    height: 1000px;
    overflow: hidden;
    background: var(--page-bg);
  }
  .canvas {
    position: relative;
    width: 1200px;
    height: 1000px;
  }
  .business-card {
    position: absolute;
    left: 265px;
    width: 665px;
    height: 397px;
    background: var(--card-bg);
    border-radius: 22px;
    overflow: hidden;
    box-shadow: 0 4px 14px var(--card-shadow);
    font-family: "Figtree", sans-serif;
    color: var(--ink);
  }
  .business-card--top { top: 73px; }
  .business-card--bottom { top: 532px; }

  .brand-mark {
    position: absolute;
    left: 40px;
    top: 62px;
    width: 92px;
    height: 92px;
    border-radius: 50%;
    background: var(--accent);
  }
  .brand-name {
    position: absolute;
    left: 158px;
    top: 84px;
    font-weight: 800;
    color: var(--ink);
    line-height: 1;
  }
  .brand-name__title {
    display: block;
    font-size: 36px;
    letter-spacing: 1px;
    text-transform: uppercase;
  }
  .brand-name__suffix {
    display: block;
    margin-top: 4px;
    font-size: 13px;
    letter-spacing: 2.4px;
    text-transform: uppercase;
  }

  .contact {
    position: absolute;
    left: 158px;
    top: 186px;
  }
  .contact__person {
    font-size: 18px;
    font-weight: 500;
    color: var(--accent);
    margin-bottom: 12px;
  }
  .contact__line {
    display: flex;
    align-items: center;
    gap: 8px;
    font-size: 15.5px;
    line-height: 22px;
  }
  .contact__icon {
    width: 14px;
    height: 14px;
    flex: none;
  }
  .services {
    margin-top: 14px;
    font-size: 15.5px;
    line-height: 20.5px;
  }

  .card-band {
    position: absolute;
    left: 0;
    bottom: 0;
    width: 100%;
    height: 19px;
    background: linear-gradient(90deg, var(--flame-red) 0%, var(--flame-orange) 25%, var(--flame-yellow) 48%, var(--flame-orange) 75%, var(--flame-red) 100%);
  }
</style>
</head>
<body>
<main class="canvas">

  <article class="business-card business-card--top">
    <div class="brand-mark"></div>
    <div class="brand-name">
      <span class="brand-name__title">Brindle Works</span>
      <span class="brand-name__suffix">PTY LTD</span>
    </div>
    <section class="contact">
      <p class="contact__person">Dale Morrow</p>
      <p class="contact__line">
        <svg class="contact__icon" viewBox="0 0 24 24" aria-hidden="true"><path fill="#ee6a1c" d="M6.6 10.8a15.1 15.1 0 0 0 6.6 6.6l2.2-2.2a1 1 0 0 1 1-.25 11.4 11.4 0 0 0 3.6.57 1 1 0 0 1 1 1V20a1 1 0 0 1-1 1A17 17 0 0 1 3 4a1 1 0 0 1 1-1h3.5a1 1 0 0 1 1 1c0 1.25.2 2.45.57 3.57a1 1 0 0 1-.25 1z"/></svg>
        07 5981 4726
      </p>
      <p class="contact__line">
        <svg class="contact__icon" viewBox="0 0 24 24" aria-hidden="true"><rect x="2" y="5" width="20" height="14" rx="1.5" fill="#ee6a1c"/><path d="M3 6.5l9 6.5 9-6.5" fill="none" stroke="#fff" stroke-width="1.6"/></svg>
        admin@brindleworks-example.com.au
      </p>
      <p class="services">
        Install all types of gas appliances &amp;<br>
        equipment inc. hot water units<br>
        Maintain / repair / replace all types of<br>
        gas appliances &amp; equipment
      </p>
    </section>
    <div class="card-band"></div>
  </article>

  <article class="business-card business-card--bottom">
    <div class="brand-mark"></div>
    <div class="brand-name">
      <span class="brand-name__title">Brindle Works</span>
      <span class="brand-name__suffix">PTY LTD</span>
    </div>
    <section class="contact">
      <p class="contact__person">Dale Morrow</p>
      <p class="contact__line">
        <svg class="contact__icon" viewBox="0 0 24 24" aria-hidden="true"><path fill="#ee6a1c" d="M6.6 10.8a15.1 15.1 0 0 0 6.6 6.6l2.2-2.2a1 1 0 0 1 1-.25 11.4 11.4 0 0 0 3.6.57 1 1 0 0 1 1 1V20a1 1 0 0 1-1 1A17 17 0 0 1 3 4a1 1 0 0 1 1-1h3.5a1 1 0 0 1 1 1c0 1.25.2 2.45.57 3.57a1 1 0 0 1-.25 1z"/></svg>
        07 5981 4726
      </p>
      <p class="contact__line">
        <svg class="contact__icon" viewBox="0 0 24 24" aria-hidden="true"><rect x="2" y="5" width="20" height="14" rx="1.5" fill="#ee6a1c"/><path d="M3 6.5l9 6.5 9-6.5" fill="none" stroke="#fff" stroke-width="1.6"/></svg>
        admin@brindleworks-example.com.au
      </p>
      <p class="services">
        Install all types of gas appliances &amp;<br>
        equipment inc. hot water units<br>
        Maintain / repair / replace all types of<br>
        gas appliances &amp; equipment
      </p>
    </section>
    <div class="card-band"></div>
  </article>

</main>
</body>
</html>
```